Design Labels and Brand Look For Mens Soap Company

We are developing a mens soap line for a natural body wash and exfoliating bar. We will be selling this with our line of mens toiletry bags that we sell under the name of Corvane Totes on Quillmart. We are looking for you to design the product brand look with brand color palette and fonts.

The title for the mens body was is "Body Wash For Men". The title for the soap bar is "Exfoliating Bar Soap For Men"

We are providing the templates for these 2 items in PDF form. The final version of the design needs to be in a layered PSD format. You also need to send us the fonts used.

This soap will be sold on Quillmart. Do a search for "men's body wash" and "mens soap bar" you will see our competition on page one. We need to stand out with colors and design differentiaon.

Target Market(s)

Men

Industry/Entity Type

Skin Care Product

Requirements
Must have
• Layered PSD file with all fonts

```html
<!DOCTYPE html>
<html lang="en">
<head>
<meta charset="utf-8">
<title>Corvane Totes – Men's Body Wash & Bar Soap Labels</title>
<link href="https://fonts.googleapis.com/css2?family=Oswald:wght@400;500;600&family=Roboto+Condensed:wght@400;700&family=Montserrat:wght@700&family=Playfair+Display:ital@1&display=swap" rel="stylesheet">
<style>
:root{
  --navy:#0c1a33;
  --maroon:#5a0015;
  --gold:#d4b06a;
  --cream:#f4ead4;
  --white:#ffffff;
  --bottle:#e9eef2;
  --soap:#dcc08c;
}
*{box-sizing:border-box;margin:0;padding:0}
html,body{width:1200px;height:601px;overflow:hidden}
body{position:relative;font-family:"Roboto Condensed",sans-serif;background:var(--navy)}
.row{position:absolute;left:0;width:1200px}
.row--maroon{top:0;height:300px;background:var(--maroon)}
.row--navy{top:300px;height:301px;background:var(--navy)}

/* product mockup placeholders */
.mock-bottle{position:absolute;left:68px;width:97px;height:228px;border-radius:26px 26px 10px 10px;background:linear-gradient(180deg,var(--gold) 0 14%,var(--bottle) 14% 40%,var(--label-tone) 40% 82%,var(--bottle) 82%)}
.row--maroon .mock-bottle{--label-tone:var(--navy);top:31px}
.row--navy .mock-bottle{--label-tone:var(--maroon);top:40px}
.mock-soap{position:absolute;left:620px;width:155px;height:82px;border-radius:48% 52% 40% 44%;background:radial-gradient(ellipse at 45% 35%,#e8d3a6,var(--soap) 70%,#c3a571)}
.row--maroon .mock-soap{top:117px}
.row--navy .mock-soap{top:112px}

/* body wash flat label */
.wash-label{position:absolute;left:221px;width:311px;height:166px;border-top:7px solid var(--gold);border-bottom:7px solid var(--gold);color:var(--gold)}
.row--maroon .wash-label{top:94px;background:var(--navy)}
.row--navy .wash-label{top:104px;background:var(--maroon)}
.wash-label .side{position:absolute;top:50%;transform-origin:center;font-size:5px;line-height:1.35;color:var(--white);white-space:nowrap;text-align:center}
.wash-label .side--contact{left:-50px;width:150px;transform:translateY(-50%) rotate(90deg)}
.wash-label .side--contact .flag{display:inline-block;width:9px;height:6px;background:linear-gradient(var(--white),var(--white)) ;border:1px solid #b22234;vertical-align:middle;margin-right:3px}
.wash-label .side--usage{left:406px;width:150px;transform:translate(-50%,-50%) rotate(-90deg);left:268px;white-space:normal;width:150px;font-size:5px}
.brand{font-family:"Oswald",sans-serif;font-weight:500;color:var(--white);letter-spacing:.2px}
.brand-mark{display:inline-block;border:1px solid var(--white);border-radius:50%;vertical-align:middle}
.wash-label .brand-lockup{position:absolute;left:0;right:0;top:10px;text-align:center}
.wash-label .brand-lockup .brand{font-size:13px}
.wash-label .brand-lockup .brand-mark{width:9px;height:9px;margin-left:4px}
.wash-label .tagline{position:absolute;left:113px;top:82px;transform:translate(-50%,-50%) rotate(-90deg);width:80px;text-align:center;line-height:1}
.tagline .script{font-family:"Playfair Display",serif;font-style:italic;font-size:9px;color:var(--gold)}
.tagline .script small{font-family:"Roboto Condensed",sans-serif;font-style:normal;font-size:4px}
.tagline .areas{display:block;font-family:"Montserrat",sans-serif;font-size:5px;color:var(--white);letter-spacing:.6px}
.wash-label .rule{position:absolute;left:129px;top:46px;width:1px;height:74px;background:var(--gold)}
.wash-label .title{position:absolute;left:135px;top:44px;font-family:"Oswald",sans-serif;line-height:.92;color:var(--gold)}
.title .kicker{display:block;font-size:12.5px;font-weight:500}
.title .main{display:block;font-size:35px;font-weight:600;letter-spacing:-.3px}
.title .for{display:block;font-family:"Montserrat",sans-serif;font-size:10px;color:var(--white);margin-top:2px}
.wash-label .blurb{position:absolute;left:90px;width:130px;top:133px;text-align:center;font-size:4.3px;color:var(--white);line-height:1.3}
.wash-label .size{position:absolute;left:0;right:0;top:148px;text-align:center;font-family:"Oswald",sans-serif;font-size:5.5px;color:var(--white)}

/* colour palette swatches */
.palette{position:absolute;top:264px;width:66px}
.palette--left{left:534px}.palette--right{left:1134px}
.swatch{height:17px;margin-bottom:2px}
.swatch--navy{background:var(--navy)}
.swatch--gold{background:var(--gold)}
.swatch--maroon{background:var(--maroon)}
.swatch--white{background:var(--white)}

/* soap box dieline */
.soap-box{position:absolute;color:var(--gold);overflow:hidden}
.soap-box--narrow{left:779px;width:118px;height:239px;font-size:10px}
.soap-box--wide{left:912px;width:204px;height:255px;font-size:11px}
.row--maroon .soap-box{background:var(--navy);--band:var(--maroon)}
.row--navy .soap-box{background:var(--maroon);--band:var(--navy)}
.row--maroon .soap-box--narrow{top:33px}.row--maroon .soap-box--wide{top:17px}
.row--navy .soap-box--narrow{top:37px}.row--navy .soap-box--wide{top:29px}
.flip{transform:rotate(180deg)}
.soap-box .flap-copy{position:absolute;top:1.5%;left:8%;right:8%;font-size:.26em;color:var(--white);text-align:center;line-height:1.3}
.soap-box .flap-band{position:absolute;top:6%;left:0;right:0;height:4.5%;background:var(--band);font-family:"Oswald",sans-serif;font-size:.45em;color:var(--white);display:flex;align-items:center;justify-content:center;letter-spacing:.5px}
.soap-box--wide .flap-band{left:20%;right:20%;top:8%;height:3.5%}
.soap-box .flap-line{position:absolute;top:12%;left:0;right:0;text-align:center;font-family:"Oswald",sans-serif;font-size:.9em;font-weight:500;white-space:nowrap}
.soap-box .back-title{position:absolute;top:22%;left:14%;font-family:"Oswald",sans-serif;font-weight:500;line-height:.9;font-size:1.2em}
.soap-box--wide .back-title{left:30%}
.back-title small,.front-title small,.lower-title small{display:block;font-family:"Montserrat",sans-serif;font-size:.42em;color:var(--white)}
.soap-box .brand{font-size:.55em}
.soap-box .brand-mark{width:.5em;height:.5em;margin:0 .3em}
.soap-box .spine-band{position:absolute;left:7%;top:37%;width:10%;height:29%;background:var(--band);display:flex;align-items:center;justify-content:center}
.soap-box--wide .spine-band{left:27%;width:6%;top:36%;height:25%}
.spine-band span{transform:rotate(-90deg);white-space:nowrap;font-family:"Oswald",sans-serif;font-size:.55em;color:var(--white);letter-spacing:.6px}
.soap-box .front{position:absolute;left:25%;top:39%;width:68%}
.soap-box--wide .front{left:37%;width:56%;top:38%}
.front .brand{display:block;margin-bottom:.3em}
.front-title{font-family:"Oswald",sans-serif;font-weight:500;line-height:.92;font-size:1.55em}
.front .desc{margin-top:.5em;font-size:.27em;color:var(--white);line-height:1.35}
.soap-box .lower{position:absolute;left:14%;top:72%;display:flex;align-items:center;gap:.5em}
.soap-box--wide .lower{left:32%}
.lower-title{font-family:"Oswald",sans-serif;font-weight:500;line-height:.92;font-size:1.25em}
.soap-box .base-copy{position:absolute;top:85%;left:45%;right:6%;font-size:.22em;color:var(--white);line-height:1.35;text-align:right}
.soap-box--wide .base-copy{left:50%;right:14%}
.soap-box .flag{position:absolute;top:84%;right:6%;width:.9em;height:.6em;background:repeating-linear-gradient(#b22234 0 1px,var(--white) 1px 2px)}
.soap-box--wide .flag{right:14%;top:83%}
</style>
</head>
<body>

<section class="row row--maroon">
  <div class="mock-bottle" role="img" aria-label="Bottle mockup with navy body wash label and gold cap"></div>

  <article class="wash-label">
    <p class="side side--contact"><span class="flag"></span>MADE IN USA &nbsp; CORVANE TOTES<br>Address Line 1, Address Line 2, Address Line 3, Address Line 4<br>0123456789 | www.corvanetotes.com | hello@corvanetotes.com</p>
    <div class="brand-lockup"><span class="brand">Corvane</span><span class="brand-mark"></span></div>
    <p class="tagline"><span class="script">Premium Wash <small>FOR</small></span><span class="areas">HAIR - FACE - BODY</span></p>
    <span class="rule"></span>
    <h1 class="title"><span class="kicker">MOISTURIZING</span><span class="main">BODY<br>WASH</span><span class="for">For Men</span></h1>
    <p class="blurb">Enriched With Shea Butter, Cocoa Butter, Grapeseed Oil, and Jojoba Oil to moisturize, revitalize and deep clean your skin.</p>
    <p class="size">16 FL OZ (473 ML)</p>
    <p class="side side--usage">Pour a small amount of our luxurious hand soap into palm of your hand and rub together under water for a rich cleansing lather.<br>Contains: Water, Sodium Laureth Sulfate, Vegetable Glycerine, Sodium Chloride, Fragrance, Citric Acid, Sodium Benzoate, Potassium Sorbate, Vitamin E, Cocoa Butter, Shea Butter, Virgin Olive Oil, Grapeseed Oil, Colours.</p>
  </article>

  <div class="palette palette--left"><div class="swatch swatch--navy"></div><div class="swatch swatch--gold"></div><div class="swatch swatch--maroon"></div><div class="swatch swatch--white"></div></div>

  <div class="mock-soap" role="img" aria-label="Tan exfoliating soap bar with embossed brand name"></div>

  <article class="soap-box soap-box--narrow">
    <p class="flap-copy flip">Triple Milled Soap enriched with shea butter and cocoa butter, blended with wheat bran &amp; apricot seed to exfoliate and deep clean your skin.</p>
    <p class="flap-band flip">Revitalize Your Skin</p>
    <p class="flap-line flip"><span class="brand-mark"></span> EXFOLIATING BAR SOAP</p>
    <h3 class="back-title flip"><span class="brand">Corvane</span> EXFOLIATING<br>BAR SOAP<small>For Men</small></h3>
    <div class="spine-band"><span>Revitalize Your Skin</span></div>
    <div class="front"><span class="brand">Corvane</span><h2 class="front-title">EXFOLIATING<br>BAR SOAP<small>For Men</small></h2><p class="desc">Triple Milled Soap Enriched with Shea Butter and Cocoa Butter, Blended With Wheat Bran &amp; Apricot Seed to exfoliate, revitalize, and deep clean your skin.</p></div>
    <div class="lower"><span class="brand">Corvane</span><h3 class="lower-title">EXFOLIATING<br>BAR SOAP<small>For Men</small></h3></div>
    <span class="flag"></span>
    <p class="base-copy flip">INGREDIENTS: Sodium palmate, sodium cocoate, water, glycerin, wheat bran, apricot seed, fragrance. CORVANE TOTES 0123456789</p>
  </article>

  <article class="soap-box soap-box--wide">
    <p class="flap-copy flip">Triple Milled Soap enriched with shea butter and cocoa butter, blended with wheat bran &amp; apricot seed to exfoliate and deep clean your skin.</p>
    <p class="flap-band flip">Revitalize Your Skin</p>
    <p class="flap-line flip"><span class="brand-mark"></span> EXFOLIATING BAR SOAP</p>
    <h3 class="back-title flip"><span class="brand">Corvane</span> EXFOLIATING<br>BAR SOAP<small>For Men</small></h3>
    <div class="spine-band"><span>Revitalize Your Skin</span></div>
    <div class="front"><span class="brand">Corvane</span><h2 class="front-title">EXFOLIATING<br>BAR SOAP<small>For Men</small></h2><p class="desc">Triple Milled Soap Enriched with Shea Butter and Cocoa Butter, Blended With Wheat Bran &amp; Apricot Seed to exfoliate, revitalize, and deep clean your skin.</p></div>
    <div class="lower"><span class="brand">Corvane</span><h3 class="lower-title">EXFOLIATING<br>BAR SOAP<small>For Men</small></h3></div>
    <span class="flag"></span>
    <p class="base-copy flip">INGREDIENTS: Sodium palmate, sodium cocoate, water, glycerin, wheat bran, apricot seed, fragrance. CORVANE TOTES 0123456789</p>
  </article>

  <div class="palette palette--right"><div class="swatch swatch--navy"></div><div class="swatch swatch--gold"></div><div class="swatch swatch--maroon"></div><div class="swatch swatch--white"></div></div>
</section>

<section class="row row--navy">
  <div class="mock-bottle" role="img" aria-label="Bottle mockup with maroon body wash label and gold cap"></div>

  <article class="wash-label">
    <p class="side side--contact"><span class="flag"></span>MADE IN USA &nbsp; CORVANE TOTES<br>Address Line 1, Address Line 2, Address Line 3, Address Line 4<br>0123456789 | www.corvanetotes.com | hello@corvanetotes.com</p>
    <div class="brand-lockup"><span class="brand">Corvane</span><span class="brand-mark"></span></div>
    <p class="tagline"><span class="script">Premium Wash <small>FOR</small></span><span class="areas">HAIR - FACE - BODY</span></p>
    <span class="rule"></span>
    <h1 class="title"><span class="kicker">MOISTURIZING</span><span class="main">BODY<br>WASH</span><span class="for">For Men</span></h1>
    <p class="blurb">Enriched With Shea Butter, Cocoa Butter, Grapeseed Oil, and Jojoba Oil to moisturize, revitalize and deep clean your skin.</p>
    <p class="size">16 FL OZ (473 ML)</p>
    <p class="side side--usage">Pour a small amount of our luxurious hand soap into palm of your hand and rub together under water for a rich cleansing lather.<br>Contains: Water, Sodium Laureth Sulfate, Vegetable Glycerine, Sodium Chloride, Fragrance, Citric Acid, Sodium Benzoate, Potassium Sorbate, Vitamin E, Cocoa Butter, Shea Butter, Virgin Olive Oil, Grapeseed Oil, Colours.</p>
  </article>

  <div class="mock-soap" role="img" aria-label="Tan exfoliating soap bar with embossed brand name"></div>

  <article class="soap-box soap-box--narrow">
    <p class="flap-copy flip">Triple Milled Soap enriched with shea butter and cocoa butter, blended with wheat bran &amp; apricot seed to exfoliate and deep clean your skin.</p>
    <p class="flap-band flip">Revitalize Your Skin</p>
    <p class="flap-line flip"><span class="brand-mark"></span> EXFOLIATING BAR SOAP</p>
    <h3 class="back-title flip"><span class="brand">Corvane</span> EXFOLIATING<br>BAR SOAP<small>For Men</small></h3>
    <div class="spine-band"><span>Revitalize Your Skin</span></div>
    <div class="front"><span class="brand">Corvane</span><h2 class="front-title">EXFOLIATING<br>BAR SOAP<small>For Men</small></h2><p class="desc">Triple Milled Soap Enriched with Shea Butter and Cocoa Butter, Blended With Wheat Bran &amp; Apricot Seed to exfoliate, revitalize, and deep clean your skin.</p></div>
    <div class="lower"><span class="brand">Corvane</span><h3 class="lower-title">EXFOLIATING<br>BAR SOAP<small>For Men</small></h3></div>
    <span class="flag"></span>
    <p class="base-copy flip">INGREDIENTS: Sodium palmate, sodium cocoate, water, glycerin, wheat bran, apricot seed, fragrance. CORVANE TOTES 0123456789</p>
  </article>

  <article class="soap-box soap-box--wide">
    <p class="flap-copy flip">Triple Milled Soap enriched with shea butter and cocoa butter, blended with wheat bran &amp; apricot seed to exfoliate and deep clean your skin.</p>
    <p class="flap-band flip">Revitalize Your Skin</p>
    <p class="flap-line flip"><span class="brand-mark"></span> EXFOLIATING BAR SOAP</p>
    <h3 class="back-title flip"><span class="brand">Corvane</span> EXFOLIATING<br>BAR SOAP<small>For Men</small></h3>
    <div class="spine-band"><span>Revitalize Your Skin</span></div>
    <div class="front"><span class="brand">Corvane</span><h2 class="front-title">EXFOLIATING<br>BAR SOAP<small>For Men</small></h2><p class="desc">Triple Milled Soap Enriched with Shea Butter and Cocoa Butter, Blended With Wheat Bran &amp; Apricot Seed to exfoliate, revitalize, and deep clean your skin.</p></div>
    <div class="lower"><span class="brand">Corvane</span><h3 class="lower-title">EXFOLIATING<br>BAR SOAP<small>For Men</small></h3></div>
    <span class="flag"></span>
    <p class="base-copy flip">INGREDIENTS: Sodium palmate, sodium cocoate, water, glycerin, wheat bran, apricot seed, fragrance. CORVANE TOTES 0123456789</p>
  </article>
</section>

</body>
</html>
```